Business Card Design for TrailReady

TrailReady is an online e-commerce store specializing in Outdoors Gear such as camping equipment, hunting and shooting equipment, tactical gear and more. See complete line at trailready-gear.example
Logo: http://www.trailready-gear.example/media/ID/Ready.jpg
http://www.trailready-gear.example/media/ID/TrailReady-blue.jpg

Target Market(s)

20-40 Male

Industry/Entity Type

E-Commerce

```html
<!DOCTYPE html>
<html lang="en">
<head>
<meta charset="utf-8">
<title>TrailReady Business Card</title>
<link rel="stylesheet" href="https://fonts.googleapis.com/css2?family=Alegreya:wght@700;800&family=Alegreya+Sans:wght@400;500&display=swap">
<style>
  :root {
    --navy: #213861;
    --white: #ffffff;
    --backdrop: #e9ecf0;
    --card-edge: #c9ced6;
    --ink: #213861;
    --mark-grey: #ededed;
  }
  html, body {
    margin: 0;
    padding: 0;
    width: 1200px;
    height: 1035px;
    overflow: hidden;
    background: var(--backdrop);
  }
  .canvas {
    position: relative;
    width: 1200px;
    height: 1035px;
  }
  .card {
    position: absolute;
    width: 736px;
    height: 473px;
    overflow: hidden;
    box-sizing: border-box;
  }
  /* Front side */
  .card-front {
    left: 60px;
    top: 36px;
    background: var(--navy);
  }
  .brand {
    position: absolute;
    left: 58px;
    top: 190px;
    display: flex;
    align-items: center;
    gap: 24px;
  }
  .brand-square {
    width: 68px;
    height: 68px;
    border: 4px solid var(--white);
    box-sizing: border-box;
  }
  .brand-name {
    margin: 0;
    font-family: "Alegreya", serif;
    font-weight: 800;
    font-size: 56px;
    line-height: 1;
    color: var(--white);
  }
  .brand-tagline {
    margin: 8px 0 0;
    font-family: "Alegreya Sans", sans-serif;
    font-weight: 500;
    font-size: 23px;
    letter-spacing: 1.6px;
    color: var(--white);
  }
  /* Back side */
  .card-back {
    left: 404px;
    top: 528px;
    background: var(--white);
    border: 1px solid var(--card-edge);
  }
  .back-header {
    height: 139px;
    background: var(--navy);
    position: relative;
  }
  .person-name {
    position: absolute;
    left: 41px;
    top: 64px;
    margin: 0;
    font-family: "Alegreya", serif;
    font-weight: 800;
    font-size: 40px;
    line-height: 1;
    color: var(--white);
  }
  .faint-mark {
    position: absolute;
    right: -110px;
    top: 165px;
    width: 290px;
    height: 290px;
    border-radius: 50%;
    background: var(--mark-grey);
  }
  .contact {
    position: absolute;
    margin: 0;
  }
  .contact dt {
    font-family: "Alegreya", serif;
    font-weight: 700;
    font-size: 18px;
    letter-spacing: 0.5px;
    color: var(--ink);
    text-transform: uppercase;
  }
  .contact dd {
    margin: 6px 0 0;
    font-family: "Alegreya Sans", sans-serif;
    font-weight: 400;
    font-size: 23px;
    letter-spacing: 0.5px;
    color: var(--ink);
    white-space: nowrap;
  }
  .contact-address   { left: 41px;  top: 172px; }
  .contact-cell      { left: 41px;  top: 283px; }
  .contact-phone     { left: 41px;  top: 369px; }
  .contact-email     { left: 318px; top: 283px; }
  .contact-website   { left: 318px; top: 369px; }
</style>
</head>
<body>
<div class="canvas">
  <section class="card card-front" aria-label="Card front">
    <div class="brand">
      <div class="brand-square" aria-hidden="true"></div>
      <div>
        <p class="brand-name">TrailReady</p>
        <p class="brand-tagline">Equipped for Survival and Adventure</p>
      </div>
    </div>
  </section>

  <section class="card card-back" aria-label="Card back">
    <div class="back-header">
      <h1 class="person-name">Daniel Rusk</h1>
    </div>
    <div class="faint-mark" aria-hidden="true"></div>
    <dl class="contact contact-address">
      <dt>Address:</dt>
      <dd>USA, IL, Cedar Falls, PO Box 218</dd>
    </dl>
    <dl class="contact contact-cell">
      <dt>Cellphone:</dt>
      <dd>+(0)555 010 274</dd>
    </dl>
    <dl class="contact contact-phone">
      <dt>Telephone:</dt>
      <dd>+(0)555 010 274</dd>
    </dl>
    <dl class="contact contact-email">
      <dt>Email:</dt>
      <dd>danielrusk@trailready-gear.example</dd>
    </dl>
    <dl class="contact contact-website">
      <dt>Website:</dt>
      <dd>www.trailready-gear.example</dd>
    </dl>
  </section>
</div>
</body>
</html>
```